Carpet Cleaning Business Sesighn

Brio-Kleen is a carpet cleaning company we do more than carpet cleaning, carpet cleaning, upholstery cleaning, tile and grout cleaning, wood floor cleaning & refinishing, maid service, air duct cleaning, pet odor and urine removal, water restoration and carpet repair. we need a business card design for our company to match our web site http://www.brio-kleen-carpet-cleaning.example we also need our logo on our card something like our web site, colors are red, gray, black like our web site. I want the logo to pop like our web site also.
Industry/Entity Type
Business
Contact Information for Business Card
Brio-Kleen Carpet Cleaning
Martin Odsway
7182 Bellcroft Rd Halden Park, IL 60917
President
Office 555 730-1962
Cell 555 284-6157
Email Martin@Brio-Kleen-Carpet-Cleaning.example
www.brio-kleen-carpet-cleaning.example

```html
<!DOCTYPE html>
<html lang="en">
<head>
<meta charset="utf-8">
<title>Brio-Kleen Carpet Cleaning – Business Card</title>
<link href="https://fonts.googleapis.com/css2?family=Tinos:wght@400;700&display=swap" rel="stylesheet">
<style>
  :root {
    --backdrop: #1d1d1d;
    --card: #ffffff;
    --brand-red: #6b1016;
    --name-red: #7a1a1f;
    --logo-gray: #5c5c5c;
    --text-gray: #4a4a4a;
  }
  * { margin: 0; padding: 0; box-sizing: border-box; }
  html, body {
    width: 1200px; height: 1200px; overflow: hidden;
    background: var(--backdrop);
    font-family: "Tinos", "Times New Roman", serif;
  }
  .sheet {
    width: 1200px; height: 1200px;
    display: flex; flex-direction: column; align-items: center; justify-content: center;
    gap: 60px;
  }
  .card {
    position: relative;
    width: 880px; height: 503px;
    background: var(--card);
    border-radius: 28px;
    overflow: hidden;
  }
  .card-shape { position: absolute; inset: 0; width: 100%; height: 100%; }
  .brand {
    position: absolute;
    display: flex; align-items: center; gap: 18px;
    font-weight: 700; color: var(--logo-gray);
    letter-spacing: 1px;
    font-size: 84px;
    white-space: nowrap;
  }
  .brand-dot {
    width: 26px; height: 26px; border-radius: 50%;
    background: var(--brand-red);
  }
  .front .brand { left: 250px; top: 180px; }
  .back .brand { left: 300px; top: 110px; }

  .phones {
    position: absolute; left: 620px; top: 290px;
    font-size: 24px; color: var(--text-gray); line-height: 38px;
  }
  .phone-line { display: flex; align-items: center; gap: 8px; }
  .phone-line svg { width: 18px; height: 18px; fill: var(--brand-red); }

  .person { position: absolute; left: 190px; top: 400px; }
  .person-name { font-size: 30px; color: var(--name-red); line-height: 36px; }
  .person-address { font-size: 22px; color: var(--text-gray); line-height: 30px; white-space: nowrap; }

  .web-contact {
    position: absolute; left: 250px; top: 270px;
    font-size: 24px; color: var(--text-gray); line-height: 38px;
    white-space: nowrap;
  }
</style>
</head>
<body>
<main class="sheet">

  <section class="card front" aria-label="Card front">
    <svg class="card-shape" viewBox="0 0 880 503" aria-hidden="true">
      <path d="M0,255 C70,110 300,22 570,0 C280,70 95,260 72,503 L0,503 Z" fill="var(--brand-red)"/>
    </svg>
    <div class="brand"><span>Brio-Kleen</span><span class="brand-dot"></span></div>
    <div class="phones">
      <div class="phone-line">
        <svg viewBox="0 0 24 24" aria-label="Office"><path d="M3 8c0-2 2-4 9-4s9 2 9 4v2h-5V8H8v2H3zM6 11h12l2 8H4z"/></svg>
        <span>555 730-1962</span>
      </div>
      <div class="phone-line">
        <svg viewBox="0 0 24 24" aria-label="Cell"><path d="M7 2h10a1 1 0 0 1 1 1v18a1 1 0 0 1-1 1H7a1 1 0 0 1-1-1V3a1 1 0 0 1 1-1zm1 3v13h8V5z"/></svg>
        <span>555 284-6157</span>
      </div>
    </div>
    <div class="person">
      <p class="person-name">Martin Odsway</p>
      <p class="person-address">7182 Bellcroft Rd Halden Park, IL 60917</p>
    </div>
  </section>

  <section class="card back" aria-label="Card back">
    <svg class="card-shape" viewBox="0 0 880 503" aria-hidden="true">
      <path d="M600,503 C750,492 855,445 880,375 L880,503 Z" fill="var(--brand-red)"/>
    </svg>
    <div class="brand"><span>Brio-Kleen</span><span class="brand-dot"></span></div>
    <div class="web-contact">
      <p>Martin@Brio-Kleen-Carpet-Cleaning.example</p>
      <p>www.brio-kleen-carpet-cleaning.example</p>
    </div>
  </section>

</main>
</body>
</html>
```